R.T.Pell Logging Web design

Our website needs a redesign. We want it to appear professional and easy to navigate. We will be adding videos and pictures to the new website. We do not sell any products on our website. It should be designed for informational purposes. Our company performs timber harvesting and forest management services. Attached is our new company logo.

www.rtpelllogging-example.com if you want to see our current website.

Industry/Entity Type

Graphic Design

Coding

Coded - Design and coding required

```html
<!DOCTYPE html>
<html lang="en">
<head>
<meta charset="utf-8">
<title>R.T.Pell Logging Company</title>
<link href="https://fonts.googleapis.com/css2?family=Source+Sans+3:wght@300;400;600;700&display=swap" rel="stylesheet">
<style>
:root{
  --gold:#e8b040;
  --gold-bar:#e4ad45;
  --brown-dark:#3f2010;
  --brown-title:#6a2e12;
  --brown-btn:#b35a22;
  --brown-btn2:#5e2c12;
  --text:#555;
  --white:#fff;
}
*{box-sizing:border-box;margin:0;padding:0}
html,body{width:1025px;height:1200px;overflow:hidden;background:#fff}
body{font-family:"Source Sans 3",sans-serif;position:relative;color:var(--text)}
.topbar{position:absolute;top:0;left:0;width:1025px;height:42px;background:linear-gradient(90deg,#2e2a24,#4a4438 45%,#2a2620);}
.topbar .estimate{position:absolute;right:74px;top:8px;display:flex;align-items:center;gap:10px;color:#ddd;font-weight:300;font-size:15px}
.topbar .estimate .num{color:var(--gold);font-size:18px;font-weight:400;margin-left:4px}
.header{position:absolute;top:42px;left:0;width:1025px;height:68px;background:#fff}
.brand{position:absolute;left:152px;top:14px;display:flex;align-items:center;gap:8px}
.brand .mark{width:38px;height:38px;background:var(--gold)}
.brand .name{font-size:21px;font-weight:700;color:var(--brown-title);line-height:1.05}
.nav{position:absolute;right:80px;top:26px;display:flex;gap:42px;font-size:13.5px;color:#444;text-transform:uppercase}
.nav .active{color:var(--gold);font-weight:600}
.hero{position:absolute;top:110px;left:0;width:1025px;height:347px;background:linear-gradient(180deg,#6d5a44 0%,#5a3a26 45%,#2a1a10 85%,#111 100%)}
.hero .arrow{position:absolute;top:136px;width:42px;height:42px;background:#f2f2f2;display:flex;align-items:center;justify-content:center}
.hero .tagline{position:absolute;top:218px;width:100%;text-align:center;color:#f1ece4;font-weight:300}
.hero .tagline .l1{font-size:19px}
.hero .tagline .l2{font-size:24px;margin-top:4px}
.hero .actions{position:absolute;top:295px;left:381px;display:flex;gap:8px}
.btn{width:128px;height:39px;color:#fff;font-size:12.5px;display:flex;align-items:center;justify-content:center;border-radius:2px;text-transform:uppercase}
.btn.quote{background:var(--brown-btn);box-shadow:0 3px 0 #7a3512}
.btn.contact{background:var(--brown-btn2);box-shadow:0 3px 0 #3a190a}
.welcome{position:absolute;top:482px;left:150px;width:725px;text-align:center}
.welcome h1{font-size:23px;font-weight:400;color:var(--brown-title);margin-bottom:14px}
.welcome p{font-size:12px;line-height:14.3px;font-weight:300;color:#555}
.services-title{position:absolute;top:630px;width:100%;text-align:center;font-size:20px;font-weight:400;color:#222}
.chev{position:absolute;top:742px}
.services{position:absolute;top:681px;left:160px;display:flex;gap:31px}
.service{width:155px;text-align:center}
.service .photo{width:155px;height:155px;border-radius:50%}
.service h3{margin-top:18px;font-size:13px;font-weight:400;color:var(--brown-title)}
.service p{font-size:11px;line-height:13px;color:#666;margin-top:4px}
.service .more{font-size:8.5px;font-weight:700;color:#3a1a0a;margin-top:6px}
.footer{position:absolute;top:975px;left:0;width:1025px;height:177px;background:var(--brown-dark)}
.footer .contact{position:absolute;left:153px;top:37px}
.footer h4{font-size:17px;font-weight:400;color:var(--gold)}
.footer .phone{display:flex;align-items:center;gap:8px;margin-top:8px;color:#fff;font-size:31px;font-weight:300}
.footer .hours{color:#eee;font-size:15px;font-weight:300;margin-top:8px;margin-left:3px}
.footer .news{position:absolute;left:693px;top:46px}
.footer .news p{color:#eee;font-size:14px;font-weight:300;margin-top:5px}
.signup{display:flex;margin-top:13px;border:1px solid var(--gold);width:226px;height:34px}
.signup .field{flex:1;padding-left:12px;display:flex;align-items:center;color:#bbb;font-size:12px;text-transform:uppercase}
.signup .go{width:35px;background:var(--gold);display:flex;align-items:center;justify-content:center}
.bottombar{position:absolute;top:1152px;left:0;width:1025px;height:48px;background:var(--gold-bar);color:#5a3a20;font-size:13px;font-weight:300}
.bottombar .copy{position:absolute;left:152px;top:16px;display:flex;gap:28px}
.bottombar .follow{position:absolute;right:28px;top:10px;display:flex;align-items:center;gap:11px}
.bottombar .follow span{margin-right:12px;margin-top:6px}
.social{width:26px;height:26px;border-radius:50%;background:#3a1c0c}
</style>
</head>
<body>
<div class="topbar">
  <div class="estimate">
    <svg width="22" height="22" viewBox="0 0 24 24"><path d="M6 3l3 4-2 2c1 3 4 6 7 7l2-2 4 3-2 4C10 21 3 14 2 5z" fill="none" stroke="#e8b040" stroke-width="1.8"/></svg>
    Call for a free estimate <span class="num">(555) 214-0187</span>
  </div>
</div>
<header class="header">
  <div class="brand"><div class="mark"></div><div class="name">R.T.PELL LOGGING</div></div>
  <nav class="nav"><span class="active">Home</span><span>Services</span><span>About Us</span><span>Location</span><span>Contact Us</span></nav>
</header>
<section class="hero" role="img" aria-label="Photograph of giant redwood trunks in a forest">
  <div class="arrow" style="left:0"><svg width="12" height="14" viewBox="0 0 12 14"><path d="M9 1L3 7l6 6" stroke="#333" stroke-width="2.5" fill="none"/></svg></div>
  <div class="arrow" style="right:0"><svg width="12" height="14" viewBox="0 0 12 14"><path d="M3 1l6 6-6 6" stroke="#333" stroke-width="2.5" fill="none"/></svg></div>
  <div class="tagline">
    <div class="l1">Receive high-quality professional logging and land clearing services from</div>
    <div class="l2">R.T. Pell Logging Company</div>
  </div>
  <div class="actions"><div class="btn quote">Request a Quote</div><div class="btn contact">Contact Us</div></div>
</section>
<section class="welcome">
  <h1>WELCOME TO R.T.PELL LOGGING COMPANY</h1>
  <p>R. T. Pell Logging Company provides timber harvesting and forest management services. This includes select cut, plantation thinning, and clear cut. We provide mechanical felling and delimbing services. When necessary we also still cut timber the old fashion way, with a chainsaw .Whether your tract is large or small, our team of experts can provide the resources and solutions you need to get the job done right. Our track record for consistency, timely service, and expertise will continue to keep us competitive in the East Texas timber industry. We pay top dollar for your pine and hardwood timber.</p>
</section>
<h2 class="services-title">OUR SERVICES</h2>
<svg class="chev" style="left:115px" width="20" height="32" viewBox="0 0 20 32"><path d="M17 2L3 16l14 14" stroke="#999" stroke-width="2" fill="none"/></svg>
<svg class="chev" style="left:905px" width="20" height="32" viewBox="0 0 20 32"><path d="M3 2l14 14-14 14" stroke="#999" stroke-width="2" fill="none"/></svg>
<div class="services">
  <div class="service"><div class="photo" role="img" aria-label="Photograph of a redwood trunk" style="background:radial-gradient(circle at 35% 50%,#9a4a2a,#5a3a22 60%,#6c7a4a)"></div><h3>SED DIAM NONUMMY</h3><p>Sed diam nonummy nibh euis mod tincidunt ueet doloa are aliquam erat volutpat...</p><div class="more">READMORE &gt;&gt;</div></div>
  <div class="service"><div class="photo" role="img" aria-label="Photograph of a log loader truck" style="background:linear-gradient(180deg,#d8dcdc 0%,#b8a890 45%,#8a6a48 65%,#6a5a48)"></div><h3>TINCIDUNT UT NONU</h3><p>Sed diam nonummy nibh euis mod tincidunt ueet doloa are aliquam erat volutpat...</p><div class="more">READMORE &gt;&gt;</div></div>
  <div class="service"><div class="photo" role="img" aria-label="Photograph of stacked log piles along a dirt road" style="background:linear-gradient(180deg,#d8d8d8 0%,#c9a878 50%,#9a8a74 75%,#7a6c5e)"></div><h3>DUIS SIAM NONUMMY</h3><p>Sed diam nonummy nibh euis mod tincidunt ueet doloa are aliquam erat volutpat...</p><div class="more">READMORE &gt;&gt;</div></div>
  <div class="service"><div class="photo" role="img" aria-label="Photograph of cut log ends" style="background:radial-gradient(circle,#e2b07a,#c07a40 60%,#6a3a1a)"></div><h3>TINCIDUNT UT NONU</h3><p>Sed diam nonummy nibh euis mod tincidunt ueet doloa are aliquam erat volutpat...</p><div class="more">READMORE &gt;&gt;</div></div>
</div>
<footer class="footer">
  <div class="contact">
    <h4>CONTACT US</h4>
    <div class="phone"><svg width="24" height="24" viewBox="0 0 24 24"><path d="M6 3l3 4-2 2c1 3 4 6 7 7l2-2 4 3-2 4C10 21 3 14 2 5z" fill="none" stroke="#e8b040" stroke-width="1.8"/></svg>555-214-0187</div>
    <div class="hours">Our office hours are:7am-8pm</div>
  </div>
  <div class="news">
    <h4>SIGN UP FOR NEWSLETTER</h4>
    <p>Get Latest News Updates</p>
    <div class="signup"><div class="field">Enter email address...</div><div class="go"><svg width="10" height="14" viewBox="0 0 10 14"><path d="M2 1l6 6-6 6" stroke="#3f2010" stroke-width="2" fill="none"/></svg></div></div>
  </div>
</footer>
<div class="bottombar">
  <div class="copy"><span>© 2014 R.T.PELL LOGGING</span><span>|</span><span>ALL RIGHTS RESERVED</span></div>
  <div class="follow"><span>FOLLOW US</span><div class="social"></div><div class="social"></div><div class="social"></div><div class="social"></div></div>
</div>
</body>
</html>
```